Savor and Thrive Wellbeing is being Launched and needs a business card and stationery package

I need a stationery package including business card (primary focus) , letterhead, digital letterhead, envelopes, with compliments slip, A 5 note sheet for the rebranding of my business and launch of my new website. I have a logo, like beige, brown earthy tones with a hint of red. I would also like the option of my letterhead also being printed on recycled paper in another format as well as the traditional letterhead. I do also send my letters to GPs and specialists digitally as well. I like to stand out from the usual stereotype of fruits and vegetables on business cards as I find that quite tacky and stereotypical. I want the business card to capture the essence of my logo as natural, nutrition, enjoyment, nurturing and freedom with food. I have attached the logo, and additional brief sheet on my ideas. Happy to have any background that is complementary to my theme, and what you believe would be catching. Definitely DONT'T like pink, try to pick up the darker colour in the logo please. and think too much black is a little overpowering.

Target Market(s)

clients who are interested in improving their health and wellness. Client 80% females; 20% males

Industry/Entity Type

Health And Wellness

Contact Information for Business Card

I am open to having different backgrounds as well that would complement the logo. Probably less emphasis on the heart out of the logo - just happy to keep that in the logo only please
I am also wanting two business cards - one for the appointments, one for general distribution and media distribution (both need to look consistent though) - but does give opportunity for one of the business cards to be less wordy and more striking. And the front of the business card can certainly stand out with the entire savor and thrive logo and my name and grab the attention of the receiver.
1st business card
on front:
Imogen Whitcombe
Savor and Thrive Wellbeing & logo
Nutritionist and Dietitian
Tolva Medical Centre
364 Wexley Park Rd, Carina Q 4152
Phone: (07) 3521 7094 Fax: (07) 3617 2289
Mobile: 0400 915 268
www.savorandthrivewellbeing.example
imogen@savorandthrivewellbeing.example
on back:
next appointment

……………………….. at ……………………… (possibly 4 times)
If you are unable to keep your appointment, please contact us as soon as possible (small font)
2nd business card (needs to be very eye catching and stand out)
on front: Savor and Thrive Wellbeing logo and my name
on back:
Imogen Whitcombe
address
phones, fax, website, email address

Font styles to use
Other font styles liked:
• please refer to logo

Requirements
Must have
• refreshing and simple; new and vibrant - I am rebranding my business after 20 years
• to get a feel of what is the theme - go to my new website (not completed as yet - but you will get a preliminary view) - don't do as google search as blocked - but can put into website header and it will be shown
• www.savorandthrivewellbeing.example - but please ignore the colouring of the 4 blocks under the slider on the home page - I am not wanting these colourings - they are getting updated.
Nice to have
• earthy tones, beige, hint of red, fonts to match logo if possible, organic, modern
• get inspiration from my logo please, open to having other backgrounds that complement
Should not have
• no food shots or stereotypical weight/ scales images
• no green, yellow or orange

```html
<!DOCTYPE html>
<html lang="en">
<head>
<meta charset="utf-8">
<title>Savor and Thrive Wellbeing – Business Card</title>
<link rel="stylesheet" href="https://fonts.googleapis.com/css2?family=Kaushan+Script&family=Roboto+Condensed:ital,wght@0,300;0,400;1,300;1,400&display=swap">
<style>
  :root {
    --page: #e9e5df;
    --card: #f2f1ed;
    --ink: #4a4346;
    --plum: #3b3036;
    --berry: #a63f59;
    --berry-soft: rgba(166, 63, 89, 0.12);
    --rule: #8e8689;
    --white: #ffffff;
  }
  * { box-sizing: border-box; margin: 0; padding: 0; }
  html, body {
    width: 1200px; height: 987px; overflow: hidden;
    background: var(--page);
    font-family: "Roboto Condensed", "Arial Narrow", sans-serif;
    color: var(--ink);
  }
  .card {
    position: absolute; left: 292px; width: 616px; height: 350px;
    background: var(--card);
    box-shadow: 0 2px 6px rgba(0,0,0,0.18);
    overflow: hidden;
  }
  .card--front { top: 130px; }
  .card--back { top: 505px; }

  /* Front */
  .brand {
    position: absolute; left: 30px; top: 150px; width: 250px;
    display: flex; align-items: center; gap: 10px;
  }
  .brand__dot { width: 18px; height: 18px; border-radius: 50%; background: var(--berry); flex: none; }
  .brand__name { font-size: 25px; font-weight: 400; line-height: 1.1; color: var(--plum); }
  .divider { position: absolute; left: 296px; top: 52px; width: 1px; height: 224px; background: var(--rule); opacity: .6; }
  .details { position: absolute; left: 322px; top: 52px; }
  .details__name { font-family: "Kaushan Script", cursive; font-size: 23px; color: var(--plum); line-height: 1.2; }
  .details__role { font-size: 17px; font-weight: 400; color: var(--berry); line-height: 1.25; }
  .details__email { font-size: 16px; font-style: italic; font-weight: 300; line-height: 1.3; }
  .details__address { margin-top: 11px; font-size: 16px; font-weight: 300; line-height: 1.35; }
  .contact-list { margin-top: 10px; list-style: none; font-size: 16px; font-weight: 300; line-height: 1.45; }
  .contact-list li { display: flex; align-items: center; gap: 7px; }
  .contact-list svg { width: 14px; height: 14px; fill: var(--plum); flex: none; }
  .footer-band { position: absolute; left: 0; bottom: 0; width: 616px; height: 62px; }
  .footer-band__url {
    position: absolute; left: 0; right: 0; bottom: 8px;
    text-align: center; padding-left: 80px;
    font-size: 16px; font-style: italic; font-weight: 300; color: var(--white); letter-spacing: .5px;
  }

  /* Back */
  .watermark {
    position: absolute; left: -70px; top: 40px; width: 330px; height: 330px;
    border-radius: 50%; background: var(--berry-soft);
  }
  .appointment__title {
    position: absolute; top: 54px; left: 0; right: 0; text-align: center; padding-left: 12px;
    font-size: 20px; font-weight: 400; color: var(--berry); letter-spacing: .3px;
  }
  .appointment__rows { position: absolute; left: 34px; top: 73px; width: 550px; list-style: none; }
  .appointment__row { display: flex; align-items: flex-end; height: 49px; font-size: 15px; font-weight: 400; color: var(--plum); }
  .appointment__blank { flex: 1; border-bottom: 1px dotted var(--rule); margin-bottom: 3px; }
  .appointment__blank--date { flex: 0 0 276px; }
  .appointment__at { padding: 0 4px; }
  .appointment__note {
    position: absolute; left: 0; right: 0; top: 310px; text-align: center;
    font-size: 13.5px; font-style: italic; font-weight: 300;
  }
</style>
</head>
<body>

<section class="card card--front">
  <div class="brand">
    <span class="brand__dot"></span>
    <span class="brand__name">Savor and Thrive Wellbeing</span>
  </div>

  <div class="divider"></div>

  <div class="details">
    <p class="details__name">Imogen Whitcombe</p>
    <p class="details__role">Nutritionist and Dietitian</p>
    <p class="details__email">imogen@savorandthrivewellbeing.example</p>
    <p class="details__address">Tolva Medical Centre<br>364 Wexley Park Rd<br>Marlow Q 4190</p>
    <ul class="contact-list">
      <li><svg viewBox="0 0 24 24"><path d="M6.6 10.8a15.1 15.1 0 0 0 6.6 6.6l2.2-2.2a1 1 0 0 1 1-.25 11.4 11.4 0 0 0 3.6.6 1 1 0 0 1 1 1V20a1 1 0 0 1-1 1A17 17 0 0 1 3 4a1 1 0 0 1 1-1h3.5a1 1 0 0 1 1 1c0 1.25.2 2.45.6 3.6a1 1 0 0 1-.25 1z"/></svg>(07) 3521 7094</li>
      <li><svg viewBox="0 0 24 24"><path d="M6 2h10v6H6zM3 9h18v9h-3v4H6v-4H3zm5 8v3h8v-3z"/></svg>(07) 3617 2289</li>
      <li><svg viewBox="0 0 24 24"><path d="M7 1h10a2 2 0 0 1 2 2v18a2 2 0 0 1-2 2H7a2 2 0 0 1-2-2V3a2 2 0 0 1 2-2zm0 3v15h10V4z"/></svg>0400 915 268</li>
    </ul>
  </div>

  <svg class="footer-band" viewBox="0 0 616 62" preserveAspectRatio="none" aria-hidden="true">
    <path d="M0 20 Q300 -6 616 30 L616 62 L0 62 Z" fill="#a63f59"/>
    <path d="M0 25 Q300 2 616 34 L616 62 L0 62 Z" fill="#3b3036"/>
  </svg>
  <p class="footer-band__url">www.savorandthrivewellbeing.example</p>
</section>

<section class="card card--back">
  <div class="watermark" role="img" aria-label="Faint brand shape in soft berry tone"></div>
  <h2 class="appointment__title">NEXT APPOINTMENT</h2>
  <ul class="appointment__rows">
    <li class="appointment__row"><span class="appointment__blank appointment__blank--date"></span><span class="appointment__at">at</span><span class="appointment__blank"></span></li>
    <li class="appointment__row"><span class="appointment__blank appointment__blank--date"></span><span class="appointment__at">at</span><span class="appointment__blank"></span></li>
    <li class="appointment__row"><span class="appointment__blank appointment__blank--date"></span><span class="appointment__at">at</span><span class="appointment__blank"></span></li>
    <li class="appointment__row"><span class="appointment__blank appointment__blank--date"></span><span class="appointment__at">at</span><span class="appointment__blank"></span></li>
  </ul>
  <p class="appointment__note">If you are unable to keep your appointment, please contact us as soon as possible</p>
</section>

</body>
</html>
```